Small rum distillery looking for bottle design

Small rum distillery in Estonia. Looking for bottle lable design. It should be simple but at the same time point out from the variety of other bottles.
As we are a small nordic country, design can be some how nordic or represent our country. It can also have some connection with sailing or sea as we know it pirates love it.
Bottle we are using is Corvane 540

Industry/Entity Type

food and beverage

Other font styles liked:
• Baskerville

```html
<!DOCTYPE html>
<html lang="en">
<head>
<meta charset="utf-8">
<title>Harvik Distillery – Rum Label</title>
<link rel="stylesheet" href="https://fonts.googleapis.com/css2?family=Libre+Baskerville&family=Dancing+Script:wght@600&family=Arimo&display=swap">
<style>
  :root {
    --backdrop: #dcdfe1;
    --label-white: #ffffff;
    --sea-blue: #2a6fb8;
    --ink: #3a3a3a;
    --rum-red: #d23b3b;
    --emblem-red: #a3282b;
    --sketch-light: #e4e6e8;
    --sketch-mid: #b9bdc1;
  }
  * { margin: 0; padding: 0; box-sizing: border-box; }
  html, body { width: 1200px; height: 1200px; overflow: hidden; }
  body { background: var(--backdrop); position: relative; }

  .main-label {
    position: absolute; left: 220px; top: 250px;
    width: 620px; height: 700px;
  }
  .main-label svg.label-shape { position: absolute; inset: 0; }

  .brand-mark {
    position: absolute; left: 50%; top: 78px;
    width: 84px; height: 84px; margin-left: -42px;
    border-radius: 50%; background: var(--emblem-red);
  }
  .brand-name {
    position: absolute; left: 0; right: 0; top: 178px;
    text-align: center;
    font-family: "Libre Baskerville", serif;
    font-size: 78px; letter-spacing: 4px; color: var(--ink);
    line-height: 1;
  }
  .brand-rule {
    position: absolute; left: 95px; right: 95px; top: 272px;
    height: 3px; background: var(--ink);
  }
  .brand-sub {
    position: absolute; left: 0; right: 0; top: 288px;
    text-align: center;
    font-family: "Libre Baskerville", serif;
    font-size: 27px; letter-spacing: 9px; color: var(--ink);
    padding-left: 9px;
  }
  .ship-sketch {
    position: absolute; left: 200px; top: 345px;
    width: 220px; height: 180px;
    background: radial-gradient(ellipse at center, var(--sketch-mid) 0%, var(--sketch-light) 55%, var(--label-white) 80%);
  }
  .product-line {
    position: absolute; left: 0; right: 0; top: 532px;
    text-align: center;
    font-family: "Dancing Script", cursive;
    font-weight: 600; font-size: 36px; color: var(--rum-red);
  }
  .volume-info {
    position: absolute; left: 0; right: 0; top: 622px;
    text-align: center;
    font-family: "Arimo", sans-serif;
    font-size: 21px; color: var(--label-white);
  }
  .volume-info .divider { margin: 0 14px; }

  .neck-strip {
    position: absolute; left: 900px; top: 250px;
    width: 80px; height: 300px;
    background: var(--label-white);
  }
  .neck-name {
    position: absolute; left: 50%; top: 20px;
    transform: translateX(-50%);
    writing-mode: vertical-rl;
    font-family: "Libre Baskerville", serif;
    font-size: 30px; letter-spacing: 4px; color: var(--ink);
  }
  .neck-mark {
    position: absolute; left: 50%; top: 205px;
    width: 54px; height: 54px; margin-left: -27px;
    border-radius: 50%; background: var(--emblem-red);
  }
</style>
</head>
<body>
  <section class="main-label">
    <svg class="label-shape" width="620" height="700" viewBox="0 0 620 700">
      <polygon points="0,186 310,8 620,186 620,700 0,700" fill="var(--label-white)"/>
      <polyline points="0,186 310,8 620,186" fill="none" stroke="var(--sea-blue)" stroke-width="12" stroke-linejoin="miter"/>
      <rect x="0" y="590" width="620" height="110" fill="var(--sea-blue)"/>
    </svg>

    <div class="brand-mark"></div>
    <div class="brand-name">HARVIK</div>
    <div class="brand-rule"></div>
    <div class="brand-sub">DISTILLERY</div>
    <div class="ship-sketch" role="img" aria-label="Light pencil sketch of a tall sailing ship on waves"></div>
    <div class="product-line">Estonian Distillery Rum</div>
    <div class="volume-info">500 ml<span class="divider">|</span>37.5% vol. alc.</div>
  </section>

  <aside class="neck-strip">
    <div class="neck-name">HARVIK</div>
    <div class="neck-mark"></div>
  </aside>
</body>
</html>
```